Graphic to hang inside of fitness studio

This graphic will be printed on vinyl and hung inside of a boutique fitness studio for 2019. Graphic should read YEAR OF POSSIBILITIES.

2018 was called Year of Living Well. We would like something on trend for 2019 to hang within the studio as our 2019 Mantra. It is not a logo but for internal use. I've attached our logo here and the website is www.kestrelmovehall.com for additional reference. Thank you.

Target Market(s)

25 to 45 women

Industry/Entity Type

Fitness

Colors

Designer to choose colors to be used in the design.

Requirements
Must have
• On trend for 2019. (no people in image)
• Year of Possibilities in trendy font.
• Easy to read.
• Need text only.
• Do not need graphic images.
Nice to have
• Tintorell colours for 2019
• 2019 design trends for background
Should not have
• Male dominate colour or masculine traits.
• Photos of fitness.
• Photos of people.
• Photos of equipment.

```html
<!DOCTYPE html>
<html lang="en">
<head>
<meta charset="UTF-8">
<title>Year of Possibilities</title>
<link rel="stylesheet" href="https://fonts.googleapis.com/css2?family=Yeseva+One&display=swap">
<style>
  :root {
    --sky-top: #3f93d2;
    --sky-mid: #8cc3e6;
    --horizon: #b9dbe8;
    --sea-light: #7cbdb8;
    --sea-deep: #4c9b95;
    --lettering: #ffffff;
    --star: #f3ede4;
  }
  html, body {
    margin: 0;
    padding: 0;
    overflow: hidden;
    background: #ffffff;
  }
  .poster {
    position: relative;
    width: 1014px;
    height: 1200px;
    overflow: hidden;
  }
  .poster__scene {
    position: absolute;
    inset: 0;
    background: linear-gradient(
      to bottom,
      var(--sky-top) 0%,
      var(--sky-mid) 40%,
      var(--horizon) 64%,
      var(--sea-light) 68%,
      var(--sea-deep) 100%
    );
  }
  .mantra {
    position: absolute;
    left: 0;
    right: 0;
    top: 972px;
    margin: 0;
    text-align: center;
    font-family: "Yeseva One", serif;
    font-weight: 400;
    color: var(--lettering);
    line-height: 1;
    text-shadow: 0 2px 6px rgba(0, 0, 0, 0.12);
  }
  .mantra__line {
    display: flex;
    align-items: center;
    justify-content: center;
  }
  .mantra__line--top {
    font-size: 86px;
    letter-spacing: 6px;
    gap: 14px;
  }
  .mantra__line--bottom {
    margin-top: 28px;
    font-size: 86px;
    letter-spacing: 4px;
  }
  .stars {
    display: flex;
    gap: 9px;
    margin-top: 30px;
  }
  .stars svg {
    width: 23px;
    height: 23px;
    fill: var(--star);
  }
</style>
</head>
<body>
  <main class="poster">
    <div class="poster__scene" role="img" aria-label="Photograph of a tall limestone sea stack topped with green shrubs, rising from calm turquoise water under a blue sky with distant karst islands"></div>

    <h1 class="mantra">
      <span class="mantra__line mantra__line--top">
        <span class="stars" aria-hidden="true">
          <svg viewBox="0 0 24 24"><polygon points="12,1 15,9 23,9 16.5,14 19,22 12,17 5,22 7.5,14 1,9 9,9"/></svg>
          <svg viewBox="0 0 24 24"><polygon points="12,1 15,9 23,9 16.5,14 19,22 12,17 5,22 7.5,14 1,9 9,9"/></svg>
          <svg viewBox="0 0 24 24"><polygon points="12,1 15,9 23,9 16.5,14 19,22 12,17 5,22 7.5,14 1,9 9,9"/></svg>
          <svg viewBox="0 0 24 24"><polygon points="12,1 15,9 23,9 16.5,14 19,22 12,17 5,22 7.5,14 1,9 9,9"/></svg>
        </span>
        <span class="mantra__words">YEAR OF</span>
        <span class="stars" aria-hidden="true">
          <svg viewBox="0 0 24 24"><polygon points="12,1 15,9 23,9 16.5,14 19,22 12,17 5,22 7.5,14 1,9 9,9"/></svg>
          <svg viewBox="0 0 24 24"><polygon points="12,1 15,9 23,9 16.5,14 19,22 12,17 5,22 7.5,14 1,9 9,9"/></svg>
          <svg viewBox="0 0 24 24"><polygon points="12,1 15,9 23,9 16.5,14 19,22 12,17 5,22 7.5,14 1,9 9,9"/></svg>
          <svg viewBox="0 0 24 24"><polygon points="12,1 15,9 23,9 16.5,14 19,22 12,17 5,22 7.5,14 1,9 9,9"/></svg>
        </span>
      </span>
      <span class="mantra__line mantra__line--bottom">POSSIBILITIES</span>
    </h1>
  </main>
</body>
</html>
```